AV GLOSSUM BUSINESS CARD DESIGN PROJECT

We need to utilize our logo that was expertly created on Sketchloom and now need to match this with a business card design.

```html
<!DOCTYPE html>
<html lang="en">
<head>
<meta charset="utf-8">
<title>AV Glossum — Business Card</title>
<link rel="stylesheet" href="https://fonts.googleapis.com/css2?family=Anton&family=Lato:wght@400;700;900&display=swap">
<style>
  :root {
    --backdrop: #2a2a2a;
    --card-blue: #0055aa;
    --ink-white: #ffffff;
    --card-shadow: rgba(0, 0, 0, 0.45);
  }
  * { box-sizing: border-box; margin: 0; padding: 0; }
  html, body {
    width: 1200px;
    height: 875px;
    overflow: hidden;
    background: var(--backdrop);
  }
  .stage {
    width: 1200px;
    height: 875px;
    display: flex;
    align-items: center;
    justify-content: center;
    gap: 44px;
  }
  .card {
    width: 520px;
    height: 300px;
    background: var(--card-blue);
    border-radius: 22px;
    box-shadow: 0 18px 40px var(--card-shadow);
    color: var(--ink-white);
    position: relative;
  }

  /* Front */
  .card-front {
    display: flex;
    align-items: center;
    justify-content: center;
  }
  .brand {
    display: flex;
    align-items: center;
    gap: 16px;
  }
  .brand-dot {
    width: 34px;
    height: 34px;
    border-radius: 50%;
    background: var(--ink-white);
  }
  .brand-name {
    font-family: "Lato", sans-serif;
    font-weight: 900;
    font-size: 40px;
    letter-spacing: 0.18em;
    color: var(--ink-white);
  }

  /* Back */
  .card-back {
    display: flex;
    align-items: center;
    padding: 0 34px 0 40px;
  }
  .identity {
    flex: 0 0 190px;
    text-align: right;
    padding-right: 22px;
    margin-top: 70px;
  }
  .person-name {
    font-family: "Anton", sans-serif;
    font-size: 27px;
    line-height: 1.05;
    letter-spacing: 0.01em;
    text-transform: uppercase;
  }
  .person-role {
    font-family: "Lato", sans-serif;
    font-size: 16px;
    margin-top: 2px;
  }
  .divider {
    width: 1.5px;
    height: 150px;
    background: var(--ink-white);
    align-self: center;
  }
  .contact-list {
    list-style: none;
    padding-left: 22px;
    font-family: "Lato", sans-serif;
    font-size: 14px;
    line-height: 1.3;
    margin-top: -20px;
  }
  .contact-item {
    display: flex;
    align-items: center;
    gap: 10px;
    margin-bottom: 3px;
  }
  .contact-item.address { align-items: flex-start; margin-bottom: 6px; }
  .contact-item.address .icon { margin-top: 10px; }
  .icon {
    width: 12px;
    height: 12px;
    flex: 0 0 12px;
    fill: var(--ink-white);
  }
  .icon-line {
    fill: none;
    stroke: var(--ink-white);
    stroke-width: 1.2;
  }
</style>
</head>
<body>
<main class="stage">

  <section class="card card-front" aria-label="Card front">
    <div class="brand">
      <span class="brand-dot"></span>
      <span class="brand-name">AV GLOSSUM</span>
    </div>
  </section>

  <section class="card card-back" aria-label="Card back">
    <div class="identity">
      <p class="person-name">Daniel Rowe</p>
      <p class="person-role">Founder &amp; CEO</p>
    </div>
    <span class="divider"></span>
    <ul class="contact-list">
      <li class="contact-item address">
        <svg class="icon" viewBox="0 0 12 12"><path d="M6 0a4 4 0 0 0-4 4c0 3 4 8 4 8s4-5 4-8a4 4 0 0 0-4-4zm0 5.6A1.6 1.6 0 1 1 6 2.4a1.6 1.6 0 0 1 0 3.2z"/></svg>
        <span>48 Harbor Lane<br>Brookfield, ST 20418</span>
      </li>
      <li class="contact-item">
        <svg class="icon" viewBox="0 0 12 12"><path d="M2.4 0.6l2 2.2-1 1.3a7 7 0 0 0 4.5 4.5l1.3-1 2.2 2-1.2 1.8C5 11 1 7 0.6 1.8z"/></svg>
        <span>(415) 302-6618</span>
      </li>
      <li class="contact-item">
        <svg class="icon" viewBox="0 0 12 12"><path d="M3 0h6a1 1 0 0 1 1 1v10a1 1 0 0 1-1 1H3a1 1 0 0 1-1-1V1a1 1 0 0 1 1-1zm0.6 1.5v7.5h4.8V1.5z"/></svg>
        <span>(415) 302-6619</span>
      </li>
      <li class="contact-item">
        <svg class="icon" viewBox="0 0 12 12"><path d="M3 0h6v3H3zM1 4h10a1 1 0 0 1 1 1v4H9.5v3h-7V9H0V5a1 1 0 0 1 1-1zm2.5 4v3h5V8z"/></svg>
        <span>(415) 302-6620</span>
      </li>
      <li class="contact-item">
        <svg class="icon" viewBox="0 0 12 12"><path d="M0 2h12v0.8L6 6.6 0 2.8zm0 2.2l6 3.8 6-3.8V10H0z"/></svg>
        <span>hello@avglossum.co</span>
      </li>
      <li class="contact-item">
        <svg class="icon" viewBox="0 0 12 12"><g class="icon-line"><circle cx="6" cy="6" r="5.2"/><ellipse cx="6" cy="6" rx="2.3" ry="5.2"/><path d="M0.8 6h10.4"/></g></svg>
        <span>www.avglossum.co</span>
      </li>
    </ul>
  </section>

</main>
</body>
</html>
```